Webbanner-Design holvira.at Webshop
Zielgruppe
Onlineshop für Haus + Garten
holvira.at
Aufgabenstellung
Benötigt wird ein neues Banner-Set
ein Allgemeines - warum bei holvira.at einkaufen
- günstige Preise durch Direktbezug ohne Zwischenhandel
- alle Artikel vorrätig - schnelle Lieferung
- Sichere Kaufabwicklung - Lumena Kauf
- Fachberatung und Service durch geschultes Peronal
sowie Banner für jede Hauptkategorie

```html
<!DOCTYPE html>
<html lang="de">
<head>
<meta charset="utf-8">
<title>holvira.at – Webshop Banner</title>
<link href="https://fonts.googleapis.com/css2?family=Fira+Sans:wght@400;600;700&family=Open+Sans:wght@400;600&display=swap" rel="stylesheet">
<style>
  :root {
    --navy: #1f3c84;
    --navy-light: #2766ad;
    --gold: #c9a55a;
    --link-blue: #3a8fd9;
    --nav-text: #555b61;
    --border: #c9ccd0;
    --white: #ffffff;
    --dark-btn: #3a3a3a;
    --pool-a: #7fb3c8;
    --pool-b: #4f8aa3;
    --pool-c: #a9c7d3;
  }
  * { box-sizing: border-box; margin: 0; padding: 0; }
  html, body { width: 1200px; height: 745px; overflow: hidden; }
  body { position: relative; background: var(--white); font-family: "Open Sans", sans-serif; }

  .header { position: absolute; left: 0; top: 0; width: 1200px; height: 110px; background: var(--white); }
  .brand { position: absolute; left: 55px; top: 36px; display: flex; align-items: center; gap: 8px; }
  .brand-square { width: 22px; height: 22px; background: var(--navy); }
  .brand-name { font-family: "Fira Sans", sans-serif; font-weight: 700; font-size: 26px; color: var(--gold); letter-spacing: -0.3px; }
  .seal { position: absolute; left: 342px; top: 36px; width: 52px; height: 52px; border-radius: 50%; background: var(--navy); border: 3px solid #e6e9ee; }

  .toplinks { position: absolute; left: 892px; top: 14px; display: flex; font-size: 12px; color: var(--link-blue); }
  .toplinks span { padding: 0 7px; border-left: 1px solid #cfd5db; line-height: 16px; }
  .toplinks span:first-child { border-left: none; padding-left: 0; }
  .lang { position: absolute; left: 1069px; top: 13px; width: 76px; height: 21px; background: var(--dark-btn); border-radius: 3px; color: var(--white); font-size: 12px; line-height: 21px; padding-left: 20px; }
  .lang::after { content: ""; position: absolute; right: 6px; top: 8px; border: 4px solid transparent; border-top-color: var(--white); }
  .lang::before { content: ""; position: absolute; left: 6px; top: 6px; width: 9px; height: 9px; border: 1px solid var(--white); }

  .search { position: absolute; left: 676px; top: 49px; width: 242px; height: 36px; border: 1px solid var(--border); border-radius: 3px; background: var(--white); }
  .search-input { position: absolute; left: 12px; top: 8px; font-size: 14px; color: #9aa0a6; }
  .search-btn { position: absolute; right: 0; top: 0; width: 40px; height: 34px; background: #eef0f2; border-left: 1px solid var(--border); }
  .search-btn svg { position: absolute; left: 11px; top: 8px; }

  .account, .cart { position: absolute; top: 65px; font-size: 14px; color: var(--link-blue); display: flex; align-items: center; gap: 4px; }
  .account { left: 947px; }
  .cart { left: 1069px; }
  .caret { width: 0; height: 0; border: 4px solid transparent; border-top-color: var(--link-blue); margin: 4px 0 0 6px; }

  .nav { position: absolute; left: 0; top: 110px; width: 1200px; height: 61px; background: linear-gradient(#ffffff, #ececec); }
  .nav-item { position: absolute; top: 21px; font-size: 14px; color: var(--nav-text); display: flex; align-items: center; }
  .nav-item .drop { width: 0; height: 0; border: 3.5px solid transparent; border-top-color: var(--nav-text); margin: 4px 0 0 3px; }

  .backdrop { position: absolute; left: 0; top: 171px; width: 1200px; height: 574px; background: linear-gradient(90deg, var(--pool-b), var(--pool-c) 25%, var(--pool-a) 60%, var(--pool-b)); }
  .panel { position: absolute; left: 50px; top: 185px; width: 1100px; height: 549px; background: var(--white); }

  .banner { position: absolute; left: 23px; top: 22px; width: 1055px; height: 439px; overflow: hidden; }
  .banner svg.shape { position: absolute; left: 0; top: 0; }
  .banner-copy { position: absolute; left: 38px; top: 0; color: var(--white); font-family: "Fira Sans", sans-serif; }
  .kicker { position: absolute; top: 34px; white-space: nowrap; font-size: 16px; letter-spacing: 0.2px; }
  .kicker b { font-weight: 700; }
  .headline { position: absolute; top: 78px; white-space: nowrap; font-size: 37px; line-height: 41px; font-weight: 700; letter-spacing: 0.3px; }
  .benefits { position: absolute; top: 178px; list-style: none; white-space: nowrap; }
  .benefits li { font-size: 23px; font-weight: 700; line-height: 28px; display: flex; align-items: center; gap: 6px; }
  .cta { position: absolute; top: 359px; width: 155px; height: 44px; background: var(--gold); color: var(--white); font-size: 12.5px; font-weight: 600; letter-spacing: 0.3px; text-align: center; line-height: 44px; }
  .price-badge { position: absolute; left: 890px; top: 274px; width: 128px; height: 128px; border-radius: 50%; background: var(--gold); color: var(--white); font-family: "Fira Sans", sans-serif; font-weight: 700; text-align: center; padding-top: 36px; }
  .price-badge .label { font-size: 11.5px; line-height: 18px; letter-spacing: 0.2px; }
  .price-badge .amount { font-size: 27px; line-height: 30px; margin-top: 2px; }

  .dots { position: absolute; left: 470px; top: 502px; display: flex; align-items: center; gap: 19px; }
  .dot { width: 6px; height: 6px; border-radius: 50%; background: #333; }
  .dot.active { width: 10px; height: 10px; background: var(--white); border: 2px solid #333; }
</style>
</head>
<body>
  <header class="header">
    <div class="brand"><span class="brand-square"></span><span class="brand-name">holvira.at</span></div>
    <div class="seal" role="img" aria-label="Gütesiegel"></div>
    <nav class="toplinks"><span>News</span><span>Kontakt</span><span>Links</span></nav>
    <div class="lang">Deutsch</div>
    <div class="search">
      <span class="search-input">Suchen</span>
      <div class="search-btn">
        <svg width="18" height="18" viewBox="0 0 18 18"><circle cx="7.5" cy="7.5" r="5.5" fill="none" stroke="#2d6fb2" stroke-width="2.4"/><line x1="11.5" y1="11.5" x2="16" y2="16" stroke="#2d6fb2" stroke-width="2.8" stroke-linecap="round"/></svg>
      </div>
    </div>
    <div class="account">
      <svg width="12" height="13" viewBox="0 0 12 13"><circle cx="6" cy="3.5" r="3.2" fill="#3a8fd9"/><path d="M0 13 C0 8 2.5 7 6 7 C9.5 7 12 8 12 13 Z" fill="#3a8fd9"/></svg>
      Anmelden<span class="caret"></span>
    </div>
    <div class="cart">
      <svg width="14" height="12" viewBox="0 0 14 12"><path d="M0 1 H2.5 L4 8 H12 L13.5 3 H3.2" fill="none" stroke="#3a8fd9" stroke-width="1.8"/><rect x="3.4" y="3" width="9.5" height="4.4" fill="#3a8fd9"/><circle cx="5" cy="10.5" r="1.3" fill="#3a8fd9"/><circle cx="11" cy="10.5" r="1.3" fill="#3a8fd9"/></svg>
      0,00 €<span class="caret"></span>
    </div>
  </header>

  <nav class="nav">
    <span class="nav-item" style="left:64px">Badezimmer<i class="drop"></i></span>
    <span class="nav-item" style="left:183px">Schwimmbecken<i class="drop"></i></span>
    <span class="nav-item" style="left:328px">Schwimmbadzubehör<i class="drop"></i></span>
    <span class="nav-item" style="left:505px">Sauna</span>
    <span class="nav-item" style="left:572px">Heizung, Solar, Klima<i class="drop"></i></span>
    <span class="nav-item" style="left:743px">Garten<i class="drop"></i></span>
    <span class="nav-item" style="left:826px">Kabelkanal</span>
    <span class="nav-item" style="left:923px">Whirlpoolzubehör<i class="drop"></i></span>
  </nav>

  <div class="backdrop" role="img" aria-label="Unscharfes Hintergrundfoto eines Schwimmbeckens"></div>

  <main class="panel">
    <section class="banner">
      <svg class="shape" width="1055" height="439" viewBox="0 0 1055 439">
        <defs>
          <linearGradient id="navyFill" x1="0" y1="0" x2="1" y2="1">
            <stop offset="0" stop-color="#1f3a80"/>
            <stop offset="1" stop-color="#2766ad"/>
          </linearGradient>
          <linearGradient id="poolFill" x1="0" y1="0" x2="0.6" y2="1">
            <stop offset="0" stop-color="#4fb0d6"/>
            <stop offset="0.45" stop-color="#c99b7a"/>
            <stop offset="1" stop-color="#c8ab86"/>
          </linearGradient>
        </defs>
        <rect width="1055" height="439" fill="url(#navyFill)"/>
        <path d="M482 0 C420 70 395 140 399 210 C404 300 440 380 478 439 L1055 439 L1055 0 Z" fill="var(--gold)"/>
        <path role="img" aria-label="Foto: lachende Familie am Beckenrand eines Pools" d="M503 0 C448 70 424 140 428 210 C432 300 462 380 500 439 L1055 439 L1055 0 Z" fill="url(#poolFill)"/>
      </svg>
      <div class="banner-copy">
        <p class="kicker"><b>IHR FACHMANN</b> FÜR BAD, POOL UND MEHR</p>
        <h1 class="headline">WILLKOMMEN<br>BEIM PROFI</h1>
        <ul class="benefits">
          <li><svg width="14" height="17" viewBox="0 0 14 17"><path d="M0 0 H6 L14 8.5 L6 17 H0 L8 8.5 Z" fill="var(--gold)"/></svg>GÜNSTIGE PREISE</li>
          <li><svg width="14" height="17" viewBox="0 0 14 17"><path d="M0 0 H6 L14 8.5 L6 17 H0 L8 8.5 Z" fill="var(--gold)"/></svg>KOMPETENTER SERVICE</li>
          <li><svg width="14" height="17" viewBox="0 0 14 17"><path d="M0 0 H6 L14 8.5 L6 17 H0 L8 8.5 Z" fill="var(--gold)"/></svg>SCHNELLE LIEFERUNG</li>
          <li><svg width="14" height="17" viewBox="0 0 14 17"><path d="M0 0 H6 L14 8.5 L6 17 H0 L8 8.5 Z" fill="var(--gold)"/></svg>SICHERES SHOPPING</li>
        </ul>
        <div class="cta">MEHR ERFAHREN</div>
      </div>
      <div class="price-badge">
        <div class="label">HOCHWERTIGES<br>ZUBEHÖR AB NUR</div>
        <div class="amount">59,99€</div>
      </div>
    </section>
    <div class="dots">
      <span class="dot"></span><span class="dot"></span><span class="dot"></span><span class="dot"></span><span class="dot active"></span><span class="dot"></span><span class="dot"></span>
    </div>
  </main>
</body>
</html>
```